Weekly Newsletter

Each week I send out a news update to the entire company updating everyone on the news and accomplishments of the week. I've been sending in an email but would like to start sending in a template that looks more professional. Either still in an email or perhaps something that can be turned into a PDF.
Each week I try to include something from each department:

• Headquarters
• MD Service
• Construction
• NOVA
• Richmond
• Hampton Roads
• Rockville
• Forestville
• Fleet
• Safety
• HR

For more info www.BrambleCrestUpkeep.com

Target Market(s)

Employees within the company. Might include an announcement area.

Industry/Entity Type

Electrical Power

Font styles to use
Sans Serif

Requirements
Must have
• Logo and style. awesome graphics

```html
<!DOCTYPE html>
<html lang="en">
<head>
<meta charset="utf-8">
<title>Bramble Crest Upkeep – Weekly Update</title>
<link href="https://fonts.googleapis.com/css2?family=Arimo:wght@400;700&display=swap" rel="stylesheet">
<style>
:root{
  --ink:#1a1a1a;
  --navy:#1b2fa8;
  --brand-red:#e3101c;
  --greeting-bg:#e0fdfd;
  --birthday:#f2ec4e;
  --anniv:#17893f;
  --caption:#3a55b4;
  --band:#c9ccd2;
  --photo-a:#d9dde3;
  --photo-b:#6d7380;
}
*{margin:0;padding:0;box-sizing:border-box}
html,body{width:848px;height:1200px;overflow:hidden;background:#fff}
body{position:relative;font-family:"Arimo",Arial,sans-serif;color:var(--ink)}
.greeting{position:absolute;left:51px;top:80px;width:409px;height:66px;background:var(--greeting-bg);padding:5px 1px;color:var(--navy)}
.greeting h1{font-weight:400;font-size:14px;letter-spacing:7px;word-spacing:20px;margin-bottom:12px}
.greeting p{font-size:12px;letter-spacing:3.2px;word-spacing:6px;color:var(--ink);line-height:16px;text-align:justify;text-align-last:justify}
.section{position:absolute;left:34px;width:444px}
.band{display:block;width:444px;height:18px;background:var(--band)}
.dept-title{display:flex;justify-content:space-between;font-weight:700;font-size:22px;margin-top:18px;padding:0 0 0 19px;height:30px;line-height:30px}
.dept-title .lead{color:var(--navy)}
.body{padding-left:17px}
.body p{font-size:12px;line-height:17px;letter-spacing:.75px;text-align:justify;text-align-last:justify;margin-bottom:17px}
.body b{font-weight:700}
.thanks{color:var(--navy);font-size:12.5px;letter-spacing:3px}
.divider{position:absolute;left:511px;top:36px;height:1118px;border-left:1.5px dashed var(--navy)}
.side{position:absolute;left:547px;width:260px}
.brand{top:72px;text-align:center;color:var(--brand-red);font-weight:700;font-size:30px;line-height:34px}
.issue-date{top:198px;color:var(--navy);font-size:13px;letter-spacing:4px;display:flex;justify-content:space-between}
.inside{top:230px;display:flex;justify-content:space-between;font-size:13px;letter-spacing:4px}
.inside span{border-bottom:1.5px dashed var(--ink)}
.contents{top:260px;text-align:center;color:var(--brand-red);font-size:12px;line-height:15.5px;list-style:none}
.label{font-size:15px;letter-spacing:11px}
.birthdays{top:367px}
.anniv{top:445px}
.bar{height:29px;margin-top:9px;font-size:12px;display:flex;align-items:center;justify-content:center}
.bar.yellow{background:var(--birthday)}
.bar.green{background:var(--anniv);color:#fff}
.jobs{top:525px}
.jobs .reward{text-align:center;font-size:11px;font-weight:700;letter-spacing:3px}
.jobs h2{font-weight:400;font-size:15px;line-height:14px}
.jobs h2 span{display:block;text-align:justify;text-align-last:justify;letter-spacing:11px;margin-right:-11px}
.jobs p{margin-top:20px;font-size:12px;line-height:15.5px;text-align:justify;text-align-last:justify}
.eom{top:771px;height:365px}
.eom .caption{background:var(--caption);color:#fff;font-size:12px;letter-spacing:1px;height:20px;display:flex;justify-content:space-between;align-items:center;padding:0 2px}
.eom .photo{height:344px;background:linear-gradient(180deg,var(--photo-a),var(--photo-b))}
</style>
</head>
<body>

<header class="greeting">
  <h1>Good Morning Everyone!!</h1>
  <p>I hope you are enjoying your weekend. Here is a brief update for last week.</p>
</header>

<section class="section" style="top:227px">
  <div class="band" role="img" aria-label="Decorative steel truss girder band"></div>
  <h2 class="dept-title"><span class="lead">R</span><span>O</span><span>C</span><span>K</span><span>V</span><span>I</span><span>L</span><span>L</span><span>E</span></h2>
  <div class="body" style="margin-top:9px">
    <p>· This week <b>Marco Delgado</b> and <b>Ivan Ortega</b> continued work on the Bradmoor Rd. construction project installing Volterra Power splice boxes, conduit, fiberglass poles, and Colonial post top fixtures. With the nice weather forecasted next week this project will be completed. They both also proceeded to set and picked up several knockdowns throughout Montgomery County.</p>
    <p>· <b>Owen Hartley</b> and <b>Dean Fuller</b> resumed progress group re-lamping in the Gaithersburg and Olney areas. They both additionally completed all of Montgomery County's 311 calls, took care of all expedited outage calls provided by county residents, as well as installing multiple fixtures.</p>
    <div class="thanks">Great week gentlemen, thank you!</div>
  </div>
</section>

<section class="section" style="top:566px">
  <div class="band" role="img" aria-label="Decorative steel truss girder band"></div>
  <h2 class="dept-title"><span class="lead">N</span><span>O</span><span>V</span><span>A</span><span style="visibility:hidden">.</span><span>O</span><span>F</span><span>F</span><span>I</span><span>C</span><span>E</span></h2>
  <div class="body" style="margin-top:11px">
    <p>· I would like to express my appreciation for everybody that helped find work for everyone in NoVA. <b>Carl Benton</b> and <b>Joanna Pruitt</b> took on <b>Trevor Malloy</b> and <b>Luis Ferrer</b> as helpers for Service for a couple of days. They are also allowing Hector Ruiz to work with service until StateRoads picks up again. Carl and I also had a nice discussion to determine the future of Gavin, who we originally planned to use to backfill Stan Kowalski. However, through effective planning, we (mostly Carl with his critical thinking skills) came up with an effective solution to keep Gavin busy on his current job and keep all other projects flowing smoothly.</p>
    <p>· <b>Dwayne Porter</b> used <b>Russell Keane</b> on a Traffic Call one day. <b>Dwayne and Hank Rollins</b> have also been in communication to find work for our construction and traffic crew. Thankfully, <b>Hank</b> allowed us to send our construction and traffic crew to work on one of their big digging projects.</p>
    <p>· I know <b>Russell</b> is close to me and what I have to say may sound biased, but with Ray on vacation, the only other employee who has rapport with Morris Baumann is <b>Russell</b>. Russell called Morris to see if we can work on the Toll Road on Thursday. Morris originally said that he would only allow work if Russell was leading it. Thankfully, Russell was able to convince Morris to let the crew work Thursday by pointing out that Stan ran a Toll Road crew before and has a lot of experience and that Wilfredo Ibarra would also be on the crew. Morris conceded and allowed work a day early.</p>
    <p>· <b>Alice Gorman</b> also provided her valuable advice and support, which helped move this process along.</p>
  </div>
</section>

<div class="divider"></div>

<div class="side brand">Bramble Crest<br>Upkeep</div>

<div class="side issue-date"><span>Sunday</span><span>19th</span><span>August</span></div>
<div class="side inside"><span>Inside</span><span>this</span><span>issue:</span></div>
<ul class="side contents">
  <li>Rockville</li><li>NOVA Office</li><li>Innovations</li><li>Project News</li><li>Marketing</li>
</ul>

<div class="side birthdays">
  <div class="label">BIRTHDAYS:</div>
  <div class="bar yellow">Sterling Stokes (Aug 1st)</div>
</div>

<div class="side anniv">
  <div class="label">ANNIVERSARIES:</div>
  <div class="bar green">Colin Farrow (Aug 3rd 3 years)</div>
</div>

<div class="side jobs">
  <div class="reward">REWARD</div>
  <h2><span>EMPLOYMENT</span><span>OPPORTUNITIES:</span></h2>
  <p>We are looking for a few Electricians and Equipment Operators for the construction department. If you refer someone to HR and we hire them you will receive $500 if they complete their 90 day probation period. Ask <b>Derek Salas</b> for details.</p>
</div>

<figure class="side eom">
  <figcaption class="caption"><span>James Whitford</span><span>EOM April 2018</span></figcaption>
  <div class="photo" role="img" aria-label="Photo of the employee of the month holding his award plaque in the office"></div>
</figure>

</body>
</html>
```